Unique business card design

We are looking for a design that reflects our unique social media and online marketing agency "Kestrel Media". We are a young agency with a focus on speakers, coaches and trainers. In other words, we support people who want to do good with their work and help other people live a happier, more successful and fulfilling life, reach as many people as possible with their work and thus have an influence. Our values are: sustainability, creating added value, individuality, proactivity. We want our clients to feel comfortable with us and that's why the relationship with them is very important to us. We want every customer to become a lifelong friend of the company. Most of our clients are premium coaches, meaning they are in the higher priced segment and expect seriousness, professionalism and quality. All of these things should reflect our business card as well. I look forward to feedback. Best regards, Tomas Wylander

```html
<!DOCTYPE html>
<html lang="en">
<head>
<meta charset="utf-8">
<title>Kestrel Media — Business Card</title>
<link rel="stylesheet" href="https://fonts.googleapis.com/css2?family=Montserrat:wght@400;600&family=Questrial&display=swap">
<style>
  :root {
    --backdrop: #1d1e23;
    --navy: #0c1648;
    --deep: #0a1f4a;
    --ocean: #0f4f80;
    --sky: #2d8fd0;
    --accent: #2a66c4;
    --ink: #1b2266;
    --paper: #ffffff;
  }
  * { box-sizing: border-box; margin: 0; padding: 0; }
  html, body {
    width: 1200px; height: 800px; overflow: hidden;
    background: var(--backdrop);
  }
  .stage {
    width: 1200px; height: 800px;
    display: flex; align-items: center; justify-content: center; gap: 60px;
  }
  .card {
    position: relative;
    width: 520px; height: 300px;
    overflow: hidden;
    box-shadow: 0 18px 40px rgba(0,0,0,.45);
  }
  .facet-fill {
    position: absolute; inset: 0;
    background:
      linear-gradient(35deg, rgba(45,143,208,.35) 0%, rgba(10,31,74,0) 45%),
      linear-gradient(145deg, var(--ocean) 0%, var(--deep) 45%, var(--navy) 70%, var(--ocean) 100%);
  }
  /* Front */
  .card-front .brand-title {
    position: absolute; inset: 0;
    display: flex; align-items: center; justify-content: center;
    font-family: "Questrial", sans-serif;
    font-size: 40px; color: var(--paper); letter-spacing: .5px;
  }
  /* Back */
  .card-back { background: var(--paper); }
  .card-back .band {
    position: absolute; left: 0; top: 0; width: 100%; height: 78px;
  }
  .logo-plate {
    position: absolute; right: 26px; top: 34px;
    width: 226px; height: 76px;
    background: var(--paper);
    display: flex; align-items: center; gap: 12px; padding-left: 12px;
  }
  .logo-plate .mark-square {
    width: 52px; height: 52px; background: var(--accent);
  }
  .logo-plate .brand-name {
    font-family: "Montserrat", sans-serif; font-weight: 600;
    font-size: 20px; color: var(--ink);
  }
  .divider {
    position: absolute; height: 1px; background: var(--accent);
  }
  .divider-long { left: 210px; right: 30px; top: 136px; }
  .divider-short { left: 26px; width: 190px; top: 214px; }
  .person {
    position: absolute; left: 26px; top: 172px;
    font-family: "Montserrat", sans-serif;
  }
  .person .name { font-weight: 600; font-size: 17px; color: var(--ink); line-height: 1.1; }
  .person .role { font-size: 13px; color: var(--accent); }
  .contacts {
    position: absolute; left: 26px; top: 224px;
    list-style: none;
    font-family: "Montserrat", sans-serif; font-size: 12px; color: var(--ink);
  }
  .contacts li { display: flex; align-items: center; gap: 8px; height: 21px; }
  .contacts svg { width: 16px; height: 16px; flex: none; }
  .address {
    position: absolute; right: 30px; top: 222px;
    text-align: right;
    font-family: "Montserrat", sans-serif; font-size: 12px; line-height: 1.5;
    color: var(--ink);
  }
</style>
</head>
<body>
<main class="stage">
  <section class="card card-front">
    <div class="facet-fill" role="img" aria-label="Faceted blue geometric crystal pattern"></div>
    <h1 class="brand-title">Kestrel Media</h1>
  </section>

  <section class="card card-back">
    <div class="band facet-fill" role="img" aria-label="Faceted blue geometric crystal band"></div>
    <div class="logo-plate">
      <span class="mark-square"></span>
      <span class="brand-name">Kestrel Media</span>
    </div>
    <span class="divider divider-long"></span>

    <div class="person">
      <p class="name">Tomas Wylander</p>
      <p class="role">Founder</p>
    </div>
    <span class="divider divider-short"></span>

    <ul class="contacts">
      <li>
        <svg viewBox="0 0 16 16" aria-hidden="true"><rect width="16" height="16" fill="#2a66c4"/><rect x="5" y="3" width="6" height="10" rx="1" fill="none" stroke="#fff" stroke-width="1.3"/></svg>
        (555) 014-2270
      </li>
      <li>
        <svg viewBox="0 0 16 16" aria-hidden="true"><rect width="16" height="16" fill="#2a66c4"/><rect x="3" y="4.5" width="10" height="7" fill="none" stroke="#fff" stroke-width="1.2"/><path d="M3 4.5 8 8.5 13 4.5" fill="none" stroke="#fff" stroke-width="1.2"/></svg>
        hello@kestrelmedia.com
      </li>
      <li>
        <svg viewBox="0 0 16 16" aria-hidden="true"><rect width="16" height="16" fill="#2a66c4"/><circle cx="8" cy="8" r="4.8" fill="none" stroke="#fff" stroke-width="1.1"/><ellipse cx="8" cy="8" rx="2" ry="4.8" fill="none" stroke="#fff" stroke-width="1"/><path d="M3.2 8h9.6" stroke="#fff" stroke-width="1"/></svg>
        www.kestrelmedia.com
      </li>
    </ul>

    <address class="address" style="font-style:normal">
      PO BOX 48 Harbour Lane<br>7th street Ashford
    </address>
  </section>
</main>
</body>
</html>
```